Small Artisan Bakery Needs a new Bread Bag Label

I'm looking for a new bread bag label design for our artisan bakery. I have attached photos of our current logo (we will be using this in the label) and pictures of our bread bag. For this project we will focus on one of our bread (100% Rye) however I would like the final final to be in a format I can edit for other bread types.

We are thinking that each bread bag will have 2 labels, our logo on top of the bread bag window (as shown in the attached photos) and simple bread description below the window.

We typically use Copperplate font however we are open to ideas as long as it keeps in alignment with our logo.

*Also note, we will not be printing the labels directly on the bag. The designs will be printed as labels that will be stuck on each bag. I would like to have the final designs formatted in a way that makes it simple to have printed at a standard printing shop.

The bag is 9.5" long, 5" wide.

The length fro the bottom of the bag window to the bottom of the bag is 2".

Top of the bag to top of the window is a little over 4".

Since these labels will be printed on label paper and manually stuck on the bag I would like them to not be take up up the whole space above or below the bag window. If the label design comes to the edge of the bag it will be very difficult to physically stick the label on the bag straight.

Thanks

Hi, The bag is 9.5" long, 5" wide. The length fro the bottom of the bag window to the bottom of the bag is 2". Top of the bag to top of the window is a little over 4". Since these labels will be printed on label paper and manually stuck on the bag I would like them to not be take up up the whole space above or below the bag window. If the label design comes to the edge of the bag it will be very difficult to physically stick the label on the bag straight. Thanks

```html
<!DOCTYPE html>
<html lang="en">
<head>
<meta charset="utf-8">
<title>Cedar Hollow Bread – Bag Labels</title>
<link rel="stylesheet" href="https://fonts.googleapis.com/css2?family=Cinzel:wght@400;600&display=swap">
<style>
  :root {
    --board-brown: #744b1f;
    --ink-brown: #7a4f22;
    --text-dark: #4a3526;
    --label-paper: #fbfaf7;
    --label-frame: #8a5a2a;
    --dimension-ink: #ffffff;
  }
  * { box-sizing: border-box; margin: 0; padding: 0; }
  html, body { width: 1200px; height: 927px; overflow: hidden; }
  body {
    background: var(--board-brown);
    font-family: "Cinzel", "Times New Roman", serif;
    position: relative;
  }
  .label {
    position: absolute;
    left: 372px;
    width: 456px;
    background: var(--label-paper);
    padding: 8px;
  }
  .label-frame {
    width: 100%;
    height: 100%;
    border: 2px solid var(--label-frame);
    display: flex;
    flex-direction: column;
    align-items: center;
    text-align: center;
    color: var(--ink-brown);
  }
  /* Top label: 3.8" x 3.9" */
  .label--logo { top: 60px; height: 468px; }
  .label--logo .label-frame { padding-top: 58px; }
  .brand-name {
    font-weight: 600;
    color: var(--ink-brown);
    letter-spacing: 0.06em;
    line-height: 1.05;
  }
  .label--logo .brand-name { font-size: 50px; }
  .since { margin-top: 44px; font-size: 24px; letter-spacing: 0.08em; }
  .rule {
    margin-top: 28px;
    width: 256px;
    border-top: 2px solid var(--ink-brown);
  }
  .social-dot { margin-top: 16px; }
  .social-url {
    margin-top: 6px;
    font-size: 14px;
    letter-spacing: 0.04em;
    color: var(--text-dark);
  }
  /* Bottom label: 3.8" x 1.9" */
  .label--description { top: 598px; height: 228px; }
  .label--description .label-frame { padding: 14px 14px 0; color: var(--text-dark); }
  .bread-name { font-size: 38px; font-weight: 400; letter-spacing: 0.03em; line-height: 1; }
  .bread-summary { margin-top: 16px; font-size: 10.5px; letter-spacing: 0.02em; }
  .label--description .brand-name { margin-top: 18px; font-size: 17px; }
  .ingredients {
    margin-top: 16px;
    display: flex;
    align-items: center;
    gap: 8px;
    text-align: left;
  }
  .ingredients-figure { font-size: 26px; }
  .ingredients-list { font-size: 11px; line-height: 1.25; letter-spacing: 0.02em; }
  /* Dimension notes */
  .dimension {
    position: absolute;
    color: var(--dimension-ink);
    font-family: "Helvetica Neue", Arial, sans-serif;
    font-size: 22px;
  }
  .dimension--vertical { transform: rotate(-90deg); transform-origin: center; }
</style>
</head>
<body>
  <section class="label label--logo" aria-label="Top bag label">
    <div class="label-frame">
      <h1 class="brand-name">Cedar Hollow<br>Bread</h1>
      <p class="since">Since: 1921</p>
      <div class="rule"></div>
      <svg class="social-dot" width="16" height="16" viewBox="0 0 16 16" aria-hidden="true">
        <circle cx="8" cy="8" r="7" fill="var(--ink-brown)"/>
      </svg>
      <p class="social-url">https://social.example/CedarHollowBread</p>
    </div>
  </section>

  <section class="label label--description" aria-label="Bottom bag label">
    <div class="label-frame">
      <h2 class="bread-name">100% Rye Bread</h2>
      <p class="bread-summary">Naturally leavened and fermented 100% Lithuanian rye bread.</p>
      <p class="brand-name">Cedar Hollow Bread</p>
      <div class="ingredients">
        <span class="ingredients-figure">100%</span>
        <span class="ingredients-list">Organic rye flour, 110 year old organic<br>rye culture, and grey Celtic sea salt</span>
      </div>
    </div>
  </section>

  <span class="dimension dimension--vertical" style="left:320px; top:280px;">3.9”</span>
  <span class="dimension" style="left:578px; top:540px;">3.8”</span>
  <span class="dimension dimension--vertical" style="left:320px; top:698px;">1.9”</span>
  <span class="dimension" style="left:578px; top:838px;">3.8”</span>
</body>
</html>
```